KORBALT

The business want a professional looking business card. We have a scetch we will add but want the extra upgrade, and would like more suggestions for variations of our business cards.

```html
<!DOCTYPE html>
<html lang="en">
<head>
<meta charset="UTF-8">
<title>KORBALT Business Card</title>
<link href="https://fonts.googleapis.com/css2?family=Marcellus&family=Montserrat:wght@500;600&display=swap" rel="stylesheet">
<style>
  :root {
    --page-bg: #e8e9eb;
    --card-bg: #141414;
    --card-edge: #0b0b0b;
    --gold: #e6c865;
    --gold-deep: #b8923a;
    --cream: #f7f1dc;
    --pattern-light: #1d1d1d;
    --pattern-dark: #0e0e0e;
  }
  * { margin: 0; padding: 0; box-sizing: border-box; }
  html, body {
    width: 850px; height: 1200px; overflow: hidden;
    background: var(--page-bg);
  }
  .sheet { position: relative; width: 850px; height: 1200px; }
  .card {
    position: absolute; left: 134px; width: 582px; height: 377px;
    border-radius: 22px; overflow: hidden;
    background: linear-gradient(135deg, var(--card-bg) 0%, #121212 60%, var(--card-edge) 100%);
  }
  .card--front { top: 139px; }
  .card--back { top: 630px; }
  .card__pattern {
    position: absolute; top: 0; right: 0; width: 135px; height: 100%;
    background: linear-gradient(180deg, var(--pattern-light) 0%, var(--pattern-dark) 50%, var(--pattern-light) 100%);
    opacity: .85;
  }
  .brand-mark {
    position: absolute; left: 0; width: 218px; top: 0; height: 100%;
    display: flex; flex-direction: column; align-items: center; justify-content: center; gap: 14px;
  }
  .brand-mark__dot {
    width: 46px; height: 46px; border-radius: 50%; background: var(--gold);
  }
  .brand-mark__name {
    font-family: "Marcellus", serif; font-size: 24px; letter-spacing: 7px;
    color: var(--gold); padding-left: 7px;
  }
  .divider {
    position: absolute; left: 218px; top: 52px; width: 1.5px; height: 274px;
    background: linear-gradient(180deg, var(--gold-deep), var(--gold), var(--gold-deep));
  }
  .details { position: absolute; left: 262px; top: 82px; }
  .company-name {
    font-family: "Marcellus", serif; font-size: 29px; letter-spacing: .5px;
    color: var(--gold); line-height: 1; white-space: nowrap;
  }
  .role {
    font-family: "Montserrat", sans-serif; font-weight: 600; font-size: 23px;
    color: var(--cream); margin-top: 12px; line-height: 1;
  }
  .person {
    font-family: "Montserrat", sans-serif; font-weight: 600; font-size: 14.5px;
    color: var(--cream); margin-top: 5px; line-height: 1;
  }
  .contacts { list-style: none; margin-top: 42px; }
  .contacts__item {
    display: flex; align-items: center; gap: 9px; height: 26.5px;
    font-family: "Montserrat", sans-serif; font-weight: 600; font-size: 15.5px;
    color: var(--cream);
  }
  .contacts__icon { width: 23px; height: 23px; flex: none; }
  .card--back .company-name {
    position: absolute; left: 0; right: 0; top: 168px;
    text-align: center; font-size: 37px;
  }
</style>
</head>
<body>
<div class="sheet">
  <section class="card card--front">
    <div class="card__pattern" role="img" aria-label="Faint embossed interlaced decorative pattern"></div>
    <div class="brand-mark">
      <span class="brand-mark__dot"></span>
      <span class="brand-mark__name">KORBALT</span>
    </div>
    <div class="divider"></div>
    <div class="details">
      <h1 class="company-name">KORBALT MARSTAD</h1>
      <p class="role">CEO &amp; Founder</p>
      <p class="person">Anders Lien Marstad</p>
      <ul class="contacts">
        <li class="contacts__item">
          <svg class="contacts__icon" viewBox="0 0 24 24"><circle cx="12" cy="12" r="12" fill="#e6c865"/><path d="M8.2 6.5c.6-.4 1.3-.3 1.7.3l1 1.6c.3.5.2 1.1-.2 1.5l-.7.6c.6 1.3 1.6 2.4 2.9 3l.6-.7c.4-.4 1-.5 1.5-.2l1.6 1c.6.4.7 1.1.3 1.7l-.6.8c-.6.8-1.7 1-2.7.6-3-1.3-5.2-3.6-6.4-6.6-.4-1 0-2 .8-2.6z" fill="#141414"/></svg>
          004791 555 204
        </li>
        <li class="contacts__item">
          <svg class="contacts__icon" viewBox="0 0 24 24"><circle cx="12" cy="12" r="12" fill="#e6c865"/><rect x="6" y="8" width="12" height="8.5" rx="1" fill="none" stroke="#141414" stroke-width="1.4"/><path d="M6.3 8.4 12 13l5.7-4.6M6.3 16.2l4-3.5M17.7 16.2l-4-3.5" fill="none" stroke="#141414" stroke-width="1.2"/></svg>
          korbalt.llc@postmail.com
        </li>
        <li class="contacts__item">
          <svg class="contacts__icon" viewBox="0 0 24 24"><circle cx="12" cy="12" r="12" fill="#e6c865"/><g fill="none" stroke="#141414" stroke-width="1.2"><circle cx="12" cy="12" r="6"/><ellipse cx="12" cy="12" rx="2.6" ry="6"/><path d="M6 12h12M7 9h10M7 15h10"/></g></svg>
          www.korbalt.llc
        </li>
      </ul>
    </div>
  </section>

  <section class="card card--back">
    <div class="card__pattern" role="img" aria-label="Faint embossed interlaced decorative pattern"></div>
    <h2 class="company-name">KORBALT MARSTAD</h2>
  </section>
</div>
</body>
</html>
```